Velmarone Website Redesign

We need a redesign of the company website.

We're a company, based in the UK, called Velmarone. We develop software for the Healthcare Industry, used by medical professionals throughout the UK on a daily basis.

We have a suite of tools that form the Velmarone Platform, and all are web-based.

We want to communicate that our software is not only innovative but is the best available, easy to use, and provides exceptional quality and RoI.

Additionally, we want our existing customers to be able to see what else we can offer them.

A site map is attached.
Updates

Hi Everyone,

As we approach the deadline for submissions, we’ve shortlisted threedesigns that we felt were the best of the submissions and have asked thedesigners to make some additional changes and produce some content pages so wecan see what’s beneath the Home page in the rest of the site.

Thank you all for your submissions – there was an awful lot ofdisagreement among everyone here over which designs we thought were best andsome of those that haven’t made it into the final three were very well liked.

Those in the final three have been messaged individually and have theirdesigns as the only non-eliminated ones showing. We would ask at this stagethat anyone not in the final three please do no further work or submitadditional designs as we are approaching the deadline and will not be able toprovide sufficient feedback to allow any changes in a short space of time.

Kind regards,
The Velmarone Team

Target Market(s)

Nurses and medical professionals in western-speaking countries, most notably in the UK.

Predominantly, we expect it will be senior medical staff that will be viewing (and using) our website - some will be existing customers and some will be new or potential customers.

Industry/Entity Type

Medical

Requirements
Must have
• Area to showcase and provide information about products.
• Company information - who we are and why you should choose us.
• News and events - blog, archive newsletters, publications, etc.
• Support section for existing customers - FAQ, Forum, Manuals.
• Contact page.
• We also feel that we'd like to have our telephone number and primary email address visible at all times, with an immediate ability for users to request a demonstration.
Nice to have
• A "My Velmarone" area would be nice at some point, though that's something for further down the line.

```html
<!DOCTYPE html>
<html lang="en">
<head>
<meta charset="utf-8">
<title>Velmarone Health – Bringing Technology to Healthcare</title>
<link rel="stylesheet" href="https://fonts.googleapis.com/css2?family=Arimo:wght@400;700&family=Roboto+Condensed:wght@700&display=swap">
<style>
:root{
  --blue:#0a84f0;
  --blue-pale:#a9cff0;
  --blue-tab:#a6cdef;
  --grey-text:#8e8e8e;
  --grey-line:#a9a9a9;
  --bar:#e9e9e9;
  --ink:#111;
  --dark-box1:#3b4651;
  --dark-box2:#1c242c;
  --blog-bg:#f6f6f1;
  --blog-green:#6a9a2a;
  --white:#fff;
}
*{box-sizing:border-box;margin:0;padding:0}
html,body{width:934px;height:1200px;overflow:hidden;background:var(--white)}
body{position:relative;font-family:"Arimo",Arial,sans-serif;color:var(--ink)}
.abs{position:absolute}

.top-bar{left:0;top:0;width:934px;height:38px;background:var(--bar);border-bottom:1px solid #d6d6d6}
.top-bar .date{left:34px;top:12px;font-size:11px;color:#9a9a9a}
.top-bar .utility{right:14px;top:14px;font-size:10.5px;color:#333;letter-spacing:.3px}
.utility span{margin:0 7px;color:#777}

.brand{left:35px;top:56px;font-size:42px;font-weight:700;color:var(--blue);letter-spacing:-.5px}
.brand-rule{left:35px;top:106px;width:886px;height:3px;background:var(--grey-line)}
.tagline{left:36px;top:116px;font-size:18px;font-weight:700;color:var(--grey-text)}
.contact{right:17px;text-align:right;font-size:18px;font-weight:700;color:var(--grey-text)}
.contact b{color:var(--blue);font-weight:400}
.contact.phone{top:80px}
.contact.email{top:114px}

.nav{left:31px;top:155px;display:flex;gap:1px}
.nav a{display:block;width:122px;height:48px;line-height:52px;text-align:center;text-decoration:none;
  font-family:"Roboto Condensed",Arial,sans-serif;font-weight:700;font-size:14px;color:var(--white);
  background:var(--blue-tab);border-radius:10px 14px 0 0}
.nav a.current{background:var(--blue)}

.stage{left:31px;top:203px;width:888px;height:394px;background:var(--blue-pale);border-radius:0 14px 14px 14px}
.hero-photo{left:51px;top:225px;width:595px;height:352px;border-radius:0 26px 0 0;
  background:linear-gradient(120deg,#dfe4ea 0%,#f4f5f7 45%,#c9ced4 75%,#3a3d42 100%)}
.stop-tab{left:12px;top:447px;width:32px;height:130px;background:var(--blue);border-radius:12px 0 0 12px}
.stop-tab span{position:absolute;left:16px;top:65px;transform:translate(-50%,-50%) rotate(-90deg);
  white-space:nowrap;color:var(--white);font-size:11px}

.promo{left:661px;width:239px;height:79px;border:2px solid #e8eef4;
  background:linear-gradient(#445260,var(--dark-box2));color:var(--white);outline:1px solid #263039}
.promo h3{position:absolute;font-size:17px;font-weight:700;letter-spacing:-.3px;line-height:17px}
.promo .more{position:absolute;font-size:10px;font-weight:700;color:#8cc6f5;letter-spacing:.4px}
.promo .icon{position:absolute}
.promo p{position:absolute;left:14px;top:28px;width:190px;font-size:9.5px;line-height:12px;color:#ddd}

.h2{font-size:26px;font-weight:400;color:#3d3d3d}
.h2 b{color:var(--blue)}
.copy{font-size:11.3px;line-height:18px;color:var(--ink)}
.copy h4{font-size:11px;font-weight:700}
.photo{background:linear-gradient(135deg,#e9ebee,#b5bcc4 60%,#5e646b)}

.login{left:693px;top:613px;width:222px;height:145px;border-radius:12px;
  background:linear-gradient(#57a6cf,#2d87b6);color:var(--white)}
.login h3{position:absolute;left:12px;top:6px;font-size:17px;font-weight:400}
.login label{position:absolute;left:12px;font-size:11px}
.login .field{position:absolute;left:12px;width:137px;height:20px;background:var(--white);border:1px solid #9cc}
.login .btn{position:absolute;left:157px;top:79px;width:62px;height:22px;border-radius:11px;border:1px solid #2c5d77;
  background:linear-gradient(#cfe8f4,#8fc0da);color:#2c4d60;font-size:13px;text-align:center;line-height:20px}
.login .small{position:absolute;left:12px;font-size:9.5px}
.login .small u{color:var(--white)}

.blog{left:695px;top:833px;width:224px;height:312px;background:var(--blog-bg);border:1px solid #d5d5cc}
.blog .head{position:absolute;left:20px;top:25px;font-size:16px;color:var(--blog-green)}
.blog .feed{display:inline-block;width:13px;height:13px;background:#f08a1f;border-radius:2px;vertical-align:-1px;margin-right:5px}
.blog ul{position:absolute;left:20px;top:55px;width:187px;list-style:none}
.blog li{height:49px;border-bottom:1px solid #d8d8d0;padding-top:1px}
.blog li strong{display:block;font-size:14px;color:#111}
.blog li small{font-size:11px;color:#333}

.footer{left:0;top:1163px;width:934px;height:37px;background:var(--bar);border-top:1px solid #d6d6d6}
</style>
</head>
<body>

<header>
  <div class="abs top-bar">
    <div class="abs date">TUESDAY, MAY 16, 2010 16:47</div>
    <div class="abs utility">HOME<span>|</span>SUPPORT<span>|</span>SITEMAP<span>|</span>HELP</div>
  </div>
  <div class="abs brand">Velmarone Health</div>
  <div class="abs brand-rule"></div>
  <div class="abs tagline">Bringing Technology to Healthcare</div>
  <div class="abs contact phone"><b>t:</b> +44 (0) 20 7946 0382</div>
  <div class="abs contact email"><b>e:</b> support@velmarone-health.co.uk</div>
  <nav class="abs nav">
    <a class="current" href="#">HOME</a><a href="#">ABOUT VELMARONE</a><a href="#">PRODUCT</a><a href="#">NEWS &amp; EVENTS</a><a href="#">SUPPORTS</a><a href="#">CONTACT US</a>
  </nav>
</header>

<section>
  <div class="abs stage"></div>
  <div class="abs hero-photo" role="img" aria-label="Photo of three smiling clinicians in white lab coats beside a microscope"></div>
  <div class="abs stop-tab"><span>STOP SLIDESHOW</span></div>

  <div class="abs promo" style="top:229px">
    <svg class="icon" style="left:12px;top:14px" width="44" height="48" viewBox="0 0 44 48">
      <rect x="4" y="4" width="16" height="16" rx="2" fill="#2f8fe0"/><rect x="22" y="10" width="16" height="16" rx="2" fill="#f0a020"/>
      <rect x="8" y="24" width="16" height="16" rx="2" fill="#e0601a"/><rect x="26" y="30" width="12" height="12" rx="2" fill="#7ab8ee"/>
    </svg>
    <h3 style="left:68px;top:30px">MY VELMARONE</h3>
    <span class="more" style="left:70px;top:56px">LEARN MORE ▸</span>
  </div>
  <div class="abs promo" style="top:320px">
    <h3 style="left:12px;top:18px">THE BEST QUALITY<br>CONNECTION!</h3>
    <span class="more" style="left:14px;top:56px">LEARN MORE ▸</span>
    <svg class="icon" style="left:186px;top:14px" width="42" height="48" viewBox="0 0 42 48">
      <path d="M8 22a14 14 0 0 1 24-9l4-4v12H24l5-5a10 10 0 0 0-17 6z" fill="#2f8fe0"/>
      <path d="M34 26a14 14 0 0 1-24 9l-4 4V27h12l-5 5a10 10 0 0 0 17-6z" fill="#f0a020"/>
    </svg>
  </div>
  <div class="abs promo" style="top:408px">
    <svg class="icon" style="left:10px;top:20px" width="50" height="40" viewBox="0 0 50 40">
      <rect x="6" y="2" width="38" height="26" rx="2" fill="#111" stroke="#aab" /><rect x="9" y="5" width="32" height="20" fill="#2a8fd8"/>
      <path d="M0 30h50l-4 6H4z" fill="#9aa4ae"/>
    </svg>
    <h3 style="left:68px;top:28px">REQUEST A DEMO</h3>
    <span class="more" style="left:70px;top:56px">LEARN MORE ▸</span>
  </div>
  <div class="abs promo" style="top:497px">
    <h3 style="left:12px;top:9px;font-size:14px">TESTIMONIALS</h3>
    <p>“Sed ut perspiciatis unde omnis iste uerror sit voluptatem accusantium dolo. ”</p>
    <span class="more" style="left:14px;top:58px">LEARN MORE ▸</span>
  </div>
</section>

<main>
  <h2 class="abs h2" style="left:32px;top:623px">Welcome To <b>Velmarone</b></h2>
  <div class="abs photo" style="left:470px;top:640px;width:204px;height:113px" role="img" aria-label="Photo of two lab scientists in safety glasses at a workstation"></div>
  <div class="abs copy" style="left:32px;top:663px;width:640px">
    <p>In today's changing environment, healthcare organisations globally are faced<br>with conflicting challenges; to reduce costs while offering improved healthcare<br>services to patients.</p>
    <p style="margin-top:2px">VELMARONE solutions exploit opportunities offered by the latest<br>&nbsp;technological advances. Our goal is to help:</p>
    <p style="margin-top:3px">• Reduce clinical errors</p>
    <p style="margin-top:4px">• Improve patient care</p>
    <p style="margin-top:4px">• Improve efficiency</p>
    <p style="margin-top:3px">With our integrated solutions, robust and secure infrastructure and by leveraging our experience, skills and &nbsp;partnerships,<br>Velmarone aims to become one of the leading international service and solution providers to the &nbsp;healthcare industry.</p>
  </div>

  <h2 class="abs h2" style="left:32px;top:890px"><b>Velmarone</b> Solutions</h2>
  <div class="abs photo" style="left:469px;top:886px;width:205px;height:114px" role="img" aria-label="Photo of a doctor with a stethoscope writing at a desk beside a monitor"></div>
  <div class="abs copy" style="left:32px;top:927px;width:640px">
    <p>Velmarone works in partnership with hospitals and healthcare &nbsp;professionals.<br>Our unique approach, our partnerships with clinical specialists and our technology<br>platform enables us to deliver highly robust and fit-for-purpose solutions.</p>
    <h4 style="margin-top:3px">Our Platform</h4>
    <p>Our technology platform, the Clinical Applications Portal, is a robust service<br>based framework that supports our accelerated application development approach. It enables interoperability and integration between<br>Velmarone software modules and other hospital/healthcare systems.</p>
    <h4 style="margin-top:3px">Our Products and Services Include</h4>
    <p style="margin-top:3px">• Clinical Systems</p>
    <p style="margin-top:4px">• Clinical Audit Tools</p>
    <p style="margin-top:4px">• Technology Services</p>
  </div>
</main>

<aside>
  <form class="abs login">
    <h3>Already a member?</h3>
    <label style="top:28px">E-mail</label><div class="field" style="top:42px"></div>
    <label style="top:62px">Password</label><div class="field" style="top:76px"></div>
    <div class="btn">Log In</div>
    <span class="small" style="top:104px">▪ Remember Me</span>
    <span class="small" style="top:120px">Forgot your password? <u>Click here</u></span>
  </form>

  <h2 class="abs h2" style="left:695px;top:796px"><b>Velmarone</b> Blog</h2>
  <div class="abs blog">
    <div class="head"><span class="feed"></span>Our Blog</div>
    <ul>
      <li><strong>Headline Blog</strong><small>April 27, 2010</small></li>
      <li><strong>Headline Blog</strong><small>April 22, 2010</small></li>
      <li><strong>Headline Blog</strong><small>April 14, 2010</small></li>
      <li><strong>Headline Blog</strong><small>April 12, 2010</small></li>
      <li><strong>Headline Blog</strong><small>March 24, 2010</small></li>
    </ul>
  </div>
</aside>

<footer class="abs footer"></footer>
</body>
</html>
```